Harbor Summit Flyer

We need a company flyer to present our company. Target group: Senior managers of hospitals / care facilities.
Please use the new text from the document "Kongressflyer.pptx".
Design: The last flyer can be used as a design basis - attached here: "Blue Lantern Flyer High Res Compressed.pdf". Please note the layout of the business card. The flyer must visually match the business card.
Logos for the references attached (KTV, Pelmora, Wendlach, Tarnford, Am Blauen Tor, Brunnwerk, Voli, KMBT).
Format: DIN A long in portrait format, front and back printed (or open to alternative suggestions if the format does not appear optimal from a design point of view)
Timing: We need the flyer as soon as possible

```html
<!DOCTYPE html>
<html lang="de">
<head>
<meta charset="utf-8">
<title>Blue Lantern Flyer</title>
<link href="https://fonts.googleapis.com/css2?family=Roboto:wght@300;400;500;700&family=Raleway:wght@300;400&display=swap" rel="stylesheet">
<style>
:root{
  --teal:#135a6e;
  --teal-dark:#0f4b5d;
  --red:#e23f33;
  --sky:#8ecae0;
  --sky-soft:#9dd0e3;
  --mist:#f4f4f5;
  --ink:#1f2328;
  --white:#ffffff;
  --canvas:#ffffff;
}
*{box-sizing:border-box;margin:0;padding:0}
html,body{width:1200px;height:2400px;overflow:hidden;background:var(--canvas)}
body{font-family:"Roboto",Arial,sans-serif;color:var(--ink);position:relative}
.sheet-slot{position:absolute;left:250px;width:700px;height:905px}
.sheet-slot.front-slot{top:225px}
.sheet-slot.back-slot{top:1250px}
.sheet{position:absolute;left:0;top:0;width:481px;height:622px;transform:scale(1.4553);transform-origin:0 0;background:var(--white);overflow:hidden;box-shadow:0 1px 4px rgba(0,0,0,.12)}
.abs{position:absolute}

/* front */
.hero{left:0;top:0;width:481px;height:185px;background:linear-gradient(135deg,#17657a 0%,var(--teal) 45%,var(--teal-dark) 100%)}
.wordmark{left:50px;top:48px;font-family:"Raleway",Arial,sans-serif;font-weight:300;font-size:19px;letter-spacing:2px;color:var(--white);display:flex;align-items:center;gap:8px}
.wordmark .dot{width:12px;height:12px;border-radius:50%;background:var(--white);display:inline-block}
.headline{left:32px;top:82px;font-size:26.5px;line-height:28px;font-weight:400;color:var(--white)}
.headline .dots{color:var(--red);font-size:14px;letter-spacing:1px;vertical-align:middle}
.about-bg{left:0;top:185px;width:481px;height:150px;background:var(--mist)}
.ask-red{left:29px;top:152px;width:212px;height:132px}
.ask-text{left:48px;top:160px;width:170px;color:var(--white);font-size:11px;line-height:12.5px}
.ask-text .rule{width:20px;height:1px;background:var(--white);margin:3px 0 6px}
.ask-text b{font-weight:700}
.ask-sky{left:29px;top:282px;width:183px;height:53px;background:var(--sky);border-radius:0 0 6px 6px;padding:7px 0 0 22px;font-size:9.5px;line-height:12px;font-weight:500}
.who{left:260px;top:195px;width:195px}
.who h3{color:var(--red);font-size:13.5px;font-weight:500;display:flex;align-items:center;gap:3px}
.who h3::before{content:"";width:24px;height:1px;background:var(--red)}
.who p{font-size:7.2px;line-height:10.3px;margin-top:6px}
.why{left:35px;top:355px;color:var(--teal);font-size:15px;font-weight:500}
.benefit{width:200px}
.benefit .title{display:flex;gap:9px;font-size:10.5px;line-height:13px;align-items:flex-start}
.tick{flex:none;width:12px;height:12px;margin-top:1px}
.benefit .note{font-size:6.8px;line-height:8.8px;margin:5px 0 0 22px}
.partner-name{left:37px;top:542px;color:#22b9b3;font-size:18px;font-weight:500;display:flex;align-items:center;gap:4px}
.partner-name .sq{width:9px;height:9px;background:#22b9b3;display:inline-block}
.partnership{left:128px;top:541px;font-size:19px;font-weight:300}
.frame-line{left:230px;top:557px;width:205px;height:24px;border-top:1px solid #b9bcc0;border-right:1px solid #b9bcc0}
.site-band{left:0;top:580px;width:481px;height:42px;background:var(--sky);display:flex;align-items:center;justify-content:center;gap:12px;font-family:"Raleway",Arial,sans-serif;font-size:18px;letter-spacing:4.5px}
.site-band svg{width:13px;height:13px}

/* back */
.positions-head{left:0;top:0;width:245px;height:82px;background:var(--mist);padding:34px 0 0 31px;font-size:12.5px;line-height:15px;font-weight:500}
.contact-col{left:245px;top:0;width:236px;height:398px;background:var(--sky)}
.contact-tail{left:265px;top:396px;width:40px;height:24px}
.group-h{color:var(--red);font-size:13.5px;font-weight:400}
.stat{display:flex;gap:8px;font-size:9.3px;line-height:11.5px;font-weight:500;margin-top:10px;margin-left:2px}
.stat svg{flex:none;width:13px;height:11px;margin-top:1px}
.roles{list-style:none;margin:13px 0 0 22px}
.roles li{display:flex;gap:7px;font-size:8.2px;line-height:10px;margin-bottom:5px}
.roles .tick{width:9px;height:9px}
.hello{left:260px;top:34px;color:var(--red);font-size:13.5px;line-height:16px}
.office{left:259px;width:215px;height:82px}
.portrait{position:absolute;left:0;top:0;width:70px;height:75px;border-radius:10px;background:linear-gradient(160deg,#d8d8d8,#5a5a5a 70%,#2a2a2a)}
.office .info{position:absolute;left:84px;top:3px}
.office h4{color:var(--red);font-size:12.5px;font-weight:400}
.office .who-name{color:var(--red);font-size:7px;line-height:8.5px;margin-top:1px}
.office .who-name.dark{color:var(--ink);font-weight:500}
.line{display:flex;align-items:center;gap:7px;margin-top:6px;font-size:9.5px}
.line.small{font-size:7px;margin-top:3px}
.line svg{width:10px;height:9px}
.divider{left:259px;width:219px;border-top:1px dotted #4c6f7d}
.refs{left:32px;top:430px;width:418px;height:190px;border:1px solid #c4c7ca;border-radius:10px}
.ref{position:absolute;display:flex;align-items:center;gap:5px;font-size:14px;font-weight:500}
.ref .mk{width:10px;height:10px;display:inline-block}
</style>
</head>
<body>

<!-- Front side -->
<div class="sheet-slot front-slot">
<section class="sheet front">
  <div class="abs hero"></div>
  <div class="abs wordmark"><span class="dot"></span>BLUE LANTERN</div>
  <h1 class="abs headline">Sie sind Leiter eines<br>Krankenhauses und suchen <span class="dots">.........</span></h1>
  <div class="abs about-bg"></div>

  <svg class="abs ask-red" viewBox="0 0 212 132" aria-hidden="true"><polygon points="0,0 212,0 190,20 183,20 183,132 0,132" fill="#e23f33"/></svg>
  <div class="abs ask-text">
    <div class="rule"></div>
    <b>medizinische Fachkräfte</b><br>für Ihre Klinik oder
    <div class="rule" style="margin-top:14px"></div>
    <b>herausragende<br>Führungskräfte für</b><br>Ihre Klinikverwaltung?
  </div>
  <div class="abs ask-sky">Möchten Sie dabei auf<br>Augenhöhe begleitet werden?<br>Wir unterstützen Sie gerne.</div>

  <div class="abs who">
    <h3>Wer sind wir?</h3>
    <p>Seit fast 30 Jahren gehört das Unternehmen Marwell / Blue Lantern zu den bedeutensten Personalberatungen im Gesundheitswesen. Die Rekrutierung von Spitzenpersonal für Kliniken ist unsere große Leidenschaft.<br>Durch den Zusammenschluss der beiden Firmen haben wir uns im letzten Jahr modernisiert, digitalisiert und für die Zukunft aufgestellt – ohne dabei die Tradition aus den Augen zu verlieren.</p>
  </div>

  <h2 class="abs why">Warum können wir Sie bestmöglich unterstützen?</h2>

  <div class="abs benefit" style="left:30px;top:397px">
    <div class="title"><svg class="tick" viewBox="0 0 12 12"><circle cx="6" cy="6" r="5.2" fill="none" stroke="#e23f33" stroke-width="1"/><path d="M3.6 6.2l1.7 1.6 3.2-3.4" fill="none" stroke="#e23f33" stroke-width="1"/></svg>Ehrlichkeit ist uns wichtig ...</div>
    <p class="note">... bei uns bekommen Sie aufrichtiges Marktfeedback und</p>
    <p class="note">... garantiert keine Versprechungen, die wir nicht halten können</p>
  </div>
  <div class="abs benefit" style="left:30px;top:476px">
    <div class="title"><svg class="tick" viewBox="0 0 12 12"><circle cx="6" cy="6" r="5.2" fill="none" stroke="#e23f33" stroke-width="1"/><path d="M3.6 6.2l1.7 1.6 3.2-3.4" fill="none" stroke="#e23f33" stroke-width="1"/></svg>Wir lieben was wir tun ...</div>
    <p class="note">... und wir arbeiten schnell, effizient und auf Augenhöhe</p>
  </div>
  <div class="abs benefit" style="left:260px;top:397px">
    <div class="title"><svg class="tick" viewBox="0 0 12 12"><circle cx="6" cy="6" r="5.2" fill="none" stroke="#e23f33" stroke-width="1"/><path d="M3.6 6.2l1.7 1.6 3.2-3.4" fill="none" stroke="#e23f33" stroke-width="1"/></svg>Wir sind Spezialisten im<br>Gesundheitswesen ...</div>
    <p class="note">... unser Team verfügt über fundiertes Marktverständnis</p>
  </div>
  <div class="abs benefit" style="left:260px;top:456px;width:210px">
    <div class="title"><svg class="tick" viewBox="0 0 12 12"><circle cx="6" cy="6" r="5.2" fill="none" stroke="#e23f33" stroke-width="1"/><path d="M3.6 6.2l1.7 1.6 3.2-3.4" fill="none" stroke="#e23f33" stroke-width="1"/></svg>Überragendes Netzwerk ...</div>
    <p class="note">... in allen Teilsektoren des Gesundheitswesens</p>
  </div>
  <div class="abs benefit" style="left:260px;top:496px">
    <div class="title"><svg class="tick" viewBox="0 0 12 12"><circle cx="6" cy="6" r="5.2" fill="none" stroke="#e23f33" stroke-width="1"/><path d="M3.6 6.2l1.7 1.6 3.2-3.4" fill="none" stroke="#e23f33" stroke-width="1"/></svg>Digital ...</div>
    <p class="note">... unsere Prozesse? Transparent! Unsere Suche für Sie 24/7 einsehbar</p>
  </div>

  <div class="abs partner-name"><span class="sq"></span>Marwell</div>
  <div class="abs partnership">Partnership</div>
  <div class="abs frame-line"></div>

  <div class="abs site-band">
    <svg viewBox="0 0 14 14"><circle cx="7" cy="7" r="6" fill="none" stroke="#1f2328" stroke-width="1"/><ellipse cx="7" cy="7" rx="2.6" ry="6" fill="none" stroke="#1f2328" stroke-width="1"/><path d="M1 7h12M2 4h10M2 10h10" stroke="#1f2328" stroke-width="1"/></svg>
    <span>bluelantern.io</span>
  </div>
</section>
</div>

<!-- Back side -->
<div class="sheet-slot back-slot">
<section class="sheet back">
  <div class="abs positions-head">Was sind typische Positionen,<br>die wir besetzen?</div>

  <div class="abs" style="left:31px;top:98px;width:210px">
    <h3 class="group-h">Medizinische Fachkräfte</h3>
    <div class="stat"><svg viewBox="0 0 13 11"><path d="M1 10C1 5 4 3.5 8 3.5V1l4.5 4L8 9V6.5C5 6.5 2.5 7.5 1 10z" fill="#135a6e"/></svg><span>100 Besetzungen in<br>vergangenen 2 Jahren in<br>sämtlichen Fachrichtungen,<br>z.B.</span></div>
    <ul class="roles">
      <li><svg class="tick" viewBox="0 0 12 12"><circle cx="6" cy="6" r="5.2" fill="none" stroke="#e23f33" stroke-width="1.2"/><path d="M3.6 6.2l1.7 1.6 3.2-3.4" fill="none" stroke="#e23f33" stroke-width="1.2"/></svg>Chefarzt Gynäkologie / Geburtshilfe</li>
      <li><svg class="tick" viewBox="0 0 12 12"><circle cx="6" cy="6" r="5.2" fill="none" stroke="#e23f33" stroke-width="1.2"/><path d="M3.6 6.2l1.7 1.6 3.2-3.4" fill="none" stroke="#e23f33" stroke-width="1.2"/></svg>Chefarzt Radiologie</li>
      <li><svg class="tick" viewBox="0 0 12 12"><circle cx="6" cy="6" r="5.2" fill="none" stroke="#e23f33" stroke-width="1.2"/><path d="M3.6 6.2l1.7 1.6 3.2-3.4" fill="none" stroke="#e23f33" stroke-width="1.2"/></svg>Chefarzt Psychiatrie</li>
    </ul>
  </div>

  <div class="abs" style="left:31px;top:241px;width:212px">
    <h3 class="group-h">Herausragende Führungskräfte</h3>
    <div class="stat"><svg viewBox="0 0 13 11"><path d="M1 10C1 5 4 3.5 8 3.5V1l4.5 4L8 9V6.5C5 6.5 2.5 7.5 1 10z" fill="#135a6e"/></svg><span>150 Besetzungen von<br>Leitungspositionen in sämtlichen<br>Geschäftsbereichen in<br>vergangenen 2 Jahren, z.B.</span></div>
    <ul class="roles">
      <li><svg class="tick" viewBox="0 0 12 12"><circle cx="6" cy="6" r="5.2" fill="none" stroke="#e23f33" stroke-width="1.2"/><path d="M3.6 6.2l1.7 1.6 3.2-3.4" fill="none" stroke="#e23f33" stroke-width="1.2"/></svg>Klinik Geschäftsführung / Vorstände</li>
      <li><svg class="tick" viewBox="0 0 12 12"><circle cx="6" cy="6" r="5.2" fill="none" stroke="#e23f33" stroke-width="1.2"/><path d="M3.6 6.2l1.7 1.6 3.2-3.4" fill="none" stroke="#e23f33" stroke-width="1.2"/></svg>Leitung Personal</li>
      <li><svg class="tick" viewBox="0 0 12 12"><circle cx="6" cy="6" r="5.2" fill="none" stroke="#e23f33" stroke-width="1.2"/><path d="M3.6 6.2l1.7 1.6 3.2-3.4" fill="none" stroke="#e23f33" stroke-width="1.2"/></svg>Leitung Qualitäts- und<br>Risikomanagement</li>
      <li><svg class="tick" viewBox="0 0 12 12"><circle cx="6" cy="6" r="5.2" fill="none" stroke="#e23f33" stroke-width="1.2"/><path d="M3.6 6.2l1.7 1.6 3.2-3.4" fill="none" stroke="#e23f33" stroke-width="1.2"/></svg>Leitung Patientenmanagement</li>
    </ul>
  </div>

  <div class="abs contact-col"></div>
  <svg class="abs contact-tail" viewBox="0 0 40 24" aria-hidden="true"><polygon points="0,0 40,0 35,24" fill="#8ecae0"/></svg>
  <h3 class="abs hello">Wir freuen uns, von Ihnen<br>zu hören!</h3>

  <div class="abs office" style="top:90px">
    <div class="portrait" role="img" aria-label="Porträtfoto der Ansprechpartnerin Büro Hamburg"></div>
    <div class="info">
      <h4>Büro Hamburg</h4>
      <p class="who-name">Dr. med. Lena<br>Hartwig</p>
      <div class="line"><svg viewBox="0 0 10 9"><path d="M2 .8l1.8 1.8-1 1.2c.6 1.2 1.5 2.1 2.6 2.6l1.2-1L8.4 7 7.3 8.3C4.2 8 1.3 5 1 1.8z" fill="none" stroke="#1f2328" stroke-width=".8"/></svg>+49 170 5550123</div>
      <div class="line small"><svg viewBox="0 0 10 9"><rect x=".6" y="1.2" width="8.8" height="6.6" fill="none" stroke="#1f2328" stroke-width=".8"/><path d="M.6 1.4L5 5l4.4-3.6" fill="none" stroke="#1f2328" stroke-width=".8"/></svg>lh@bluelantern.io</div>
    </div>
  </div>
  <div class="abs divider" style="top:186px"></div>

  <div class="abs office" style="top:198px">
    <div class="portrait" role="img" aria-label="Porträtfoto der Ansprechpartnerin Büro Wien"></div>
    <div class="info">
      <h4>Büro Wien</h4>
      <p class="who-name">Sofia Brenner</p>
      <div class="line"><svg viewBox="0 0 10 9"><path d="M2 .8l1.8 1.8-1 1.2c.6 1.2 1.5 2.1 2.6 2.6l1.2-1L8.4 7 7.3 8.3C4.2 8 1.3 5 1 1.8z" fill="none" stroke="#1f2328" stroke-width=".8"/></svg>+43 660 5550187</div>
      <div class="line small"><svg viewBox="0 0 10 9"><rect x=".6" y="1.2" width="8.8" height="6.6" fill="none" stroke="#1f2328" stroke-width=".8"/><path d="M.6 1.4L5 5l4.4-3.6" fill="none" stroke="#1f2328" stroke-width=".8"/></svg>sb@bluelantern.io</div>
    </div>
  </div>
  <div class="abs divider" style="top:292px"></div>

  <div class="abs office" style="top:306px">
    <div class="portrait" role="img" aria-label="Porträtfoto der Ansprechpartnerin Büro Düsseldorf"></div>
    <div class="info">
      <h4>Büro Düsseldorf</h4>
      <p class="who-name dark">Marie Ostrowski</p>
      <div class="line"><svg viewBox="0 0 10 9"><path d="M2 .8l1.8 1.8-1 1.2c.6 1.2 1.5 2.1 2.6 2.6l1.2-1L8.4 7 7.3 8.3C4.2 8 1.3 5 1 1.8z" fill="none" stroke="#1f2328" stroke-width=".8"/></svg>+49 171 5550246</div>
      <div class="line small"><svg viewBox="0 0 10 9"><rect x=".6" y="1.2" width="8.8" height="6.6" fill="none" stroke="#1f2328" stroke-width=".8"/><path d="M.6 1.4L5 5l4.4-3.6" fill="none" stroke="#1f2328" stroke-width=".8"/></svg>mo@bluelantern.io</div>
    </div>
  </div>

  <div class="abs refs">
    <div class="ref" style="left:36px;top:30px;color:#1d6fb5"><span class="mk" style="background:#1d6fb5"></span>Voli</div>
    <div class="ref" style="left:162px;top:30px;color:#2c3b45"><span class="mk" style="background:#2c3b45;border-radius:50%"></span>Verantis</div>
    <div class="ref" style="left:288px;top:36px;color:#16825f"><span class="mk" style="background:#16825f"></span>Aurelis</div>
    <div class="ref" style="left:32px;top:95px;color:#16825f;font-size:20px"><span class="mk" style="background:#16825f;border-radius:50%"></span>Pelmora</div>
    <div class="ref" style="left:164px;top:97px;color:#2c3b45;font-size:17px"><span class="mk" style="background:#c8232c"></span>Kestrel</div>
    <div class="ref" style="left:290px;top:88px;color:#1b3f7a;font-size:12px"><span class="mk" style="background:#1b3f7a;border-radius:50%"></span>Steinquell</div>
    <div class="ref" style="left:305px;top:106px;color:#1b3f7a;font-size:8px">KRW</div>
  </div>

  <div class="abs site-band" style="top:573px;height:49px">
    <svg viewBox="0 0 14 14"><circle cx="7" cy="7" r="6" fill="none" stroke="#1f2328" stroke-width="1"/><ellipse cx="7" cy="7" rx="2.6" ry="6" fill="none" stroke="#1f2328" stroke-width="1"/><path d="M1 7h12M2 4h10M2 10h10" stroke="#1f2328" stroke-width="1"/></svg>
    <span>bluelantern.io</span>
  </div>
</section>
</div>

</body>
</html>
```